Tobin’s letterhead for local government

I require a letterhead for quarterly communications with constituents. The colours I have used in the past are navy & green (together) so I’m happy to use similar colours for this. Please refer to business card as an example.
The letter must make reference to the position I hold which is as per below
“Clr Tobin Kellaway OAM”
And the tag line I have used in the past is “Tobin on Track”. Although I’m not sure if this would be used in a letterhead or not. Happy for this to be provided as an option.
I would like a photo in the letterhead as I believe face recognition is key as an elected member.

Target Market(s)

Political interests

Industry/Entity Type

Government Office

Font styles to use
Sans Serif

Requirements
Must have
• Politically professional. I have been an elected member for 2 years so it is expected that the letterhead conveys that. The colours of the business card is to be used.
Nice to have
• Background of photos to be manipulated or changed to make me stand out, if possible?
Should not have
• Looked like it’s cropped or undertaken by an amateur designer.

```html
<!DOCTYPE html>
<html lang="en">
<head>
<meta charset="utf-8">
<title>Tobin on Track – Letterhead</title>
<link href="https://fonts.googleapis.com/css2?family=Montserrat:wght@400;600;700&family=Lato:wght@400;700;900&display=swap" rel="stylesheet">
<style>
  :root {
    --navy: #2b5d92;
    --green: #3dbb6c;
    --ink: #565656;
    --ink-soft: #5f5f5f;
    --paper: #ffffff;
    --backdrop: #d8d8d8;
    --photo-a: #8a96a3;
    --photo-b: #9aa3a8;
    --photo-c: #7f8f9c;
  }
  * { margin: 0; padding: 0; box-sizing: border-box; }
  html, body { width: 1056px; height: 1200px; overflow: hidden; background: var(--backdrop); }
  .letterhead {
    position: absolute; left: 104px; top: 0;
    width: 848px; height: 1200px;
    background: var(--paper);
    font-family: "Lato", sans-serif;
    color: var(--ink);
  }
  .brand { position: absolute; left: 83px; top: 40px; }
  .brand-name {
    font-family: "Montserrat", sans-serif; font-weight: 700;
    font-size: 25px; line-height: 27px; color: var(--navy);
  }
  .brand-tagline {
    font-family: "Montserrat", sans-serif; font-weight: 400;
    font-size: 17px; letter-spacing: 5.2px; color: var(--green);
    margin-top: 3px; text-transform: uppercase;
  }
  .photo {
    position: absolute; top: 33px; width: 113px; height: 76px;
    border: 2px solid var(--navy); border-radius: 11px;
  }
  .photo-meeting { left: 423px; background: linear-gradient(160deg, #c9d2da, var(--photo-a) 60%, #5d6670); }
  .photo-group { left: 556px; background: linear-gradient(160deg, #d2d8dc, var(--photo-b) 55%, #4c545c); }
  .photo-portrait { left: 689px; background: linear-gradient(160deg, #b98a6e, var(--photo-c) 50%, #3f4a56); }
  .rule-green { position: absolute; left: 0; top: 130px; width: 60px; height: 9px; background: var(--green); }
  .rule-navy { position: absolute; left: 83px; top: 130px; width: 765px; height: 9px; background: var(--navy); }

  .letter { position: absolute; left: 80px; width: 688px; }
  .letter-date { top: 359px; font-family: "Montserrat", sans-serif; font-size: 18px; color: var(--ink-soft); }
  .recipient-name { top: 390px; font-family: "Montserrat", sans-serif; font-weight: 700; font-size: 30px; color: var(--ink); }
  .recipient-role { top: 435px; font-family: "Montserrat", sans-serif; font-size: 18px; color: var(--ink-soft); }
  .letter-body { top: 508px; font-size: 16px; line-height: 29.5px; text-align: justify; letter-spacing: -0.2px; }
  .letter-body p + p { margin-top: 29.5px; }
  .sign-off { top: 832px; font-size: 18px; }
  .signature {
    position: absolute; left: 82px; top: 878px; width: 86px; height: 60px;
    background: linear-gradient(135deg, #eef2f7, #dbe4ef);
  }

  .footer-rule { position: absolute; left: 80px; top: 1142px; width: 689px; height: 1.5px; background: var(--navy); }
  .contact {
    position: absolute; top: 1150px; left: 80px; width: 689px;
    display: flex; justify-content: center; gap: 18px;
    font-family: "Montserrat", sans-serif; font-size: 16.5px; color: var(--ink-soft);
  }
  .contact-item { display: flex; align-items: center; gap: 8px; }
  .contact-item svg { width: 16px; height: 16px; }
</style>
</head>
<body>
<main class="letterhead">
  <header>
    <div class="brand">
      <div class="brand-name">Clr Tobin<br>Kellaway OAM</div>
      <div class="brand-tagline">Tobin on Track</div>
    </div>
    <div class="photo photo-meeting" role="img" aria-label="Photo of Tobin at an outdoor table meeting with constituents"></div>
    <div class="photo photo-group" role="img" aria-label="Photo of Tobin standing with a group of residents outdoors"></div>
    <div class="photo photo-portrait" role="img" aria-label="Portrait photo of Tobin in a suit with city buildings behind"></div>
    <div class="rule-green"></div>
    <div class="rule-navy"></div>
  </header>

  <div class="letter letter-date">10 December, 2021</div>
  <div class="letter recipient-name">NADIA FAIRLIE</div>
  <div class="letter recipient-role">Cheif Executive Officer</div>

  <div class="letter letter-body">
    <p>Contrary to popular belief, Lorem Ipsum is not simply random text. It has roots in a piece of classical Latin literature from 45 BC, making it over 2000 years old. Harold Penvane, a Latin professor at Marlow Ridge College in Virginia, looked up one of the more obscure Latin words, consectetur.</p>
    <p>Lorem Ipsum comes from sections 1.10.32 and 1.10.33 of "de Finibus Bonorum et Malorum" (The Extremes of Good and Evil) by Varenus, written in 45 BC. This book is a treatise on the theory of ethics, very popular during the Renaissance. The first line of Lorem Ipsum.</p>
    <p>The standard chunk of Lorem Ipsum used since the 1500s is reproduced below for those interested.</p>
  </div>

  <div class="letter sign-off">Best Regards</div>
  <div class="signature" role="img" aria-label="Handwritten signature of the sender"></div>

  <footer>
    <div class="footer-rule"></div>
    <div class="contact">
      <span class="contact-item">
        <svg viewBox="0 0 16 16" aria-hidden="true"><path d="M3.5 1.5 L6 4 L4.6 5.8 C5.4 7.6 7.4 9.8 9.8 11 L11.6 9.6 L14.2 12 L12.6 14.2 C7.5 13.8 2 8.6 1.6 3.2 Z" fill="var(--navy)"/><path d="M9.5 2.2 A4.5 4.5 0 0 1 13.8 6.4 M9.3 4.5 A2.3 2.3 0 0 1 11.5 6.6" stroke="var(--navy)" stroke-width="1.3" fill="none"/></svg>
        0400 318 642
      </span>
      <span class="contact-item">
        <svg viewBox="0 0 16 16" aria-hidden="true"><rect x="1" y="3" width="14" height="10" fill="var(--navy)"/><path d="M1 3 L8 9 L15 3 M1 13 L6 8 M15 13 L10 8" stroke="#fff" stroke-width="1.1" fill="none"/></svg>
        tobin@tobinontrack.com
      </span>
      <span class="contact-item">
        <svg viewBox="0 0 16 16" aria-hidden="true"><g stroke="var(--navy)" stroke-width="1.1" fill="none"><circle cx="8" cy="8" r="6.5"/><ellipse cx="8" cy="8" rx="3" ry="6.5"/><path d="M1.5 8 H14.5 M2.5 4.8 H13.5 M2.5 11.2 H13.5"/></g></svg>
        www.tobinontrack.com
      </span>
    </div>
  </footer>
</main>
</body>
</html>
```